VelmoraTrade (Trading Platform)

We need a design of VelmoraTrade Trading Platform.

Please find attached a mock up of VelmoraTrade design this has to be redesigned based on plinor.co.uk style.

Industry/Entity Type

Digital

```html
<!DOCTYPE html>
<html lang="en">
<head>
<meta charset="utf-8">
<title>VelmoraTrade – Trading Platform</title>
<link href="https://fonts.googleapis.com/css2?family=Open+Sans:ital,wght@0,300;0,400;0,600;0,700;1,400&display=swap" rel="stylesheet">
<style>
:root{
  --blue:#0a9ad6;
  --blue-light:#dff0f8;
  --teal-dark:#1b6b8f;
  --ink:#333;
  --muted:#666;
  --row-a:#e6e6e6;
  --row-b:#d6d6d6;
  --sell:#b95c5c;
  --sell-dark:#7b3838;
  --buy:#7cb86a;
  --buy-dark:#4e7b3e;
  --red:#d9262b;
  --green:#3b8a3b;
  --ask-a:#f1e3e3;
  --ask-b:#e3cfcf;
  --bid-a:#e8f3e4;
  --bid-b:#d5e9cf;
  --footer:#48494d;
  --chart-bg:#000;
  --grid:#2e2e2e;
}
*{box-sizing:border-box;margin:0;padding:0}
html,body{width:1200px;height:926px;overflow:hidden}
body{position:relative;background:#fff;font-family:"Open Sans",Arial,sans-serif;color:var(--ink);font-size:14px}
.abs{position:absolute}

/* header */
.brand{left:21px;top:46px;display:flex;align-items:center;gap:10px;white-space:nowrap}
.brand-name{font-size:15px;font-weight:300;letter-spacing:3px;color:#222;text-transform:uppercase}
.brand-dot{width:15px;height:15px;border-radius:50%;background:var(--blue);flex:none}
.brand-divider{left:212px;top:14px;width:1px;height:78px;background:#999}
.main-nav{left:231px;top:79px;font-size:14px;color:#555;white-space:nowrap}
.login{left:717px;top:47px;display:flex;gap:6px;align-items:center}
.field{height:31px;border:1px solid #bbb;font-size:14px;color:#999;padding:6px 8px;background:#fff;white-space:nowrap}
.field.email{width:156px}.field.pass{width:155px}
.btn{height:29px;padding:0;font-size:14px;color:#fff;display:flex;align-items:center;justify-content:center;border-radius:3px;white-space:nowrap}
.btn.login-btn{background:#555;width:66px}
.btn.signup-btn{background:var(--blue);width:66px;margin-left:3px}
.forgot{left:719px;top:80px;font-size:11px;color:#777;white-space:nowrap}

/* ticker bar */
.ticker{left:0;top:110px;width:1200px;height:59px;background:var(--blue);color:#fff}
.ticker-coin{left:173px;top:11px;width:35px;height:35px;border-radius:50%;background:#fff}
.ticker-coin::after{content:"";position:absolute;left:6px;top:6px;width:23px;height:23px;border-radius:50%;background:var(--blue)}
.stat{top:8px;white-space:nowrap}
.stat-label{font-size:13px;display:block}
.stat-value{font-size:17px;display:block;margin-top:1px}
.stat-value small{font-size:13px}
.tick-sep{top:0;width:1px;height:59px;background:#3db2e2}

/* panels */
.panel{width:212px}
.panel-head{display:flex;background:var(--blue);color:#fff;font-size:19px;font-weight:300;height:31px;align-items:center}
.panel-head span{padding-left:14px}
.data-table{width:100%;border-collapse:collapse;font-size:14px}
.data-table td{height:27px;padding-left:12px;color:#333;white-space:nowrap}
.data-table tr:nth-child(odd) td{background:var(--row-a)}
.data-table tr:nth-child(even) td{background:#ededed}
.data-table td:first-child{width:107px;border-right:2px solid #fff}
.down{color:var(--red);font-weight:700;font-size:16px}
.up{color:var(--green);font-weight:700;font-size:16px}
.th-split{display:grid;grid-template-columns:107px 105px;height:31px;background:var(--blue);color:#fff;font-size:19px;font-weight:300;align-items:center}
.th-split span{padding-left:14px;height:31px;line-height:31px}
.th-split span:first-child{border-right:2px solid #fff}

/* chat */
.chat{left:26px;top:589px;height:269px;background:#e8e8e8}
.tabs{display:flex;height:30px;background:var(--blue-light);font-size:19px;font-weight:300;color:#222;border-bottom:2px solid var(--blue);white-space:nowrap}
.tabs span{padding:0 10px;line-height:29px}
.tabs .active{background:var(--blue);color:#fff}
.chat-msg{margin:0 6px;padding:9px 7px 9px;border-bottom:1px dashed #999;font-size:13px}
.chat-user{color:var(--blue);font-weight:700;display:block;line-height:16px}
.chat-text{color:#555;line-height:16px}
.chat-input{position:absolute;left:5px;top:239px;width:203px;height:24px;border:1px solid #aaa;background:#fff;font-size:12px;font-style:italic;color:#555;padding:3px 7px;white-space:nowrap}

/* chart */
.chart-panel{left:282px;top:190px;width:637px;height:468px;background:#e0e0e0}
.toolbar-item{top:12px;height:23px;background:#fff;font-size:13px;padding:2px 6px;color:#222;white-space:nowrap}
.caret{position:absolute;right:0;top:0;width:18px;height:23px;background:#ccc}
.caret::after{content:"";position:absolute;left:5px;top:9px;border:4px solid transparent;border-top:5px solid #333}
.side-caret{left:929px;top:202px;width:16px;height:19px;background:#ccc}
.side-caret::after{content:"";position:absolute;left:4px;top:7px;border:4px solid transparent;border-top:5px solid #333}
.chart-area{left:0;top:45px;width:637px;height:423px;background:var(--chart-bg)}
.select-tool{left:14px;top:9px;width:119px;height:35px;border:1px solid #555;border-radius:3px;background:#222;color:#ddd;font-size:13px;padding:8px 12px;white-space:nowrap}
.select-tool::after{content:"";position:absolute;right:0;top:0;width:20px;height:33px;border-left:1px solid #555}
.ohlc{left:357px;top:10px;color:#fff;font-size:12px;line-height:17px;white-space:nowrap}
.ohlc b{font-weight:400;color:#ccc;margin-right:6px}

/* orders */
.orders{left:282px;top:682px;width:637px;height:161px;background:#ddd}
.orders .tabs{height:30px;border-bottom:none;font-size:19px;background:var(--blue-light)}
.orders .tabs span{padding:0 14px}
.orders-table{width:100%;border-collapse:collapse;font-size:13px}
.orders-table th{background:var(--teal-dark);color:#fff;font-weight:400;text-align:left;height:27px;font-size:14px}
.orders-table td{height:27px;font-size:12px;white-space:nowrap}
.orders-table tr:nth-child(odd) td{background:#d1d1d1}
.orders-table tr:nth-child(even) td{background:#ececec}
.c1{padding-left:12px;width:105px}.c2{width:378px}.c3{width:82px}

/* trade box */
.trade{left:962px;top:190px;width:212px}
.trade-tabs{display:grid;grid-template-columns:1fr 1fr;height:28px;font-size:19px;font-weight:300;text-align:center;line-height:28px}
.trade-tabs .active{background:var(--blue);color:#fff}
.trade-tabs span:last-child{background:#cde8f4;color:#222}
.quote-row{display:grid;grid-template-columns:107px 105px;gap:0;margin-top:3px}
.quote{height:87px;position:relative;white-space:nowrap}
.quote.sell{background:var(--sell);color:#5b1212;border-right:2px solid #fff}
.quote.buy{background:var(--buy);color:#183f12}
.quote-title{position:absolute;left:10px;top:7px;font-size:14px;font-weight:700}
.quote-price{position:absolute;left:10px;top:28px;font-size:19px;font-weight:300}
.quote-price strong{font-size:24px;font-weight:700}
.quote-qty{position:absolute;left:0;bottom:0;width:100%;height:30px;line-height:30px;padding-left:10px;font-size:14px}
.sell .quote-qty{background:var(--sell-dark);color:#f0d0d0}
.buy .quote-qty{background:var(--buy-dark);color:#dff0d8}
.order-fields{display:flex;gap:10px;margin-top:8px}
.order-fields label{font-size:11px;color:#333;display:block;margin-bottom:2px}
.order-fields .field{height:24px;font-size:14px;color:#333;padding:2px 5px}

/* order book */
.book{left:962px;top:373px;width:212px}
.book-table{width:100%;border-collapse:collapse;font-size:14px}
.book-table td{height:26.8px;padding-left:12px}
.book-table td:first-child{width:107px;border-right:2px solid #fff}
.ask td{color:var(--red)}
.ask:nth-child(odd) td{background:var(--ask-a)}
.ask:nth-child(even) td{background:var(--ask-b)}
.bid td{color:var(--green)}
.bid:nth-child(odd) td{background:var(--bid-a)}
.bid:nth-child(even) td{background:var(--bid-b)}

/* footer */
.footer{left:0;top:891px;width:1200px;height:35px;background:var(--footer);color:#fff;font-size:13px;white-space:nowrap}
.footer-copy{left:28px;top:9px}
.footer-links{right:28px;top:9px;display:flex;gap:34px}
</style>
</head>
<body>

<header>
  <div class="abs brand"><span class="brand-name">VelmoraTrade</span><span class="brand-dot"></span></div>
  <div class="abs brand-divider"></div>
  <nav class="abs main-nav">Home · About · Trading · Support</nav>
  <div class="abs login">
    <div class="field email">Email</div>
    <div class="field pass">Password</div>
    <div class="btn login-btn">Log In</div>
    <div class="btn signup-btn">Sign Up</div>
  </div>
  <div class="abs forgot">Forgot your password?</div>
</header>

<section class="abs ticker">
  <div class="abs ticker-coin"></div>
  <div class="abs stat" style="left:224px"><span class="stat-label">Current Price</span><span class="stat-value">$444.13</span></div>
  <div class="abs tick-sep" style="left:340px"></div>
  <div class="abs stat" style="left:359px"><span class="stat-label">Daily Change</span><span class="stat-value">-9.54 <small>-2.10%</small></span></div>
  <div class="abs tick-sep" style="left:476px"></div>
  <div class="abs stat" style="left:506px"><span class="stat-label">Day's Range</span><span class="stat-value">$440.00 - $457.30</span></div>
  <div class="abs tick-sep" style="left:674px"></div>
  <div class="abs stat" style="left:704px"><span class="stat-label">Today's Open</span><span class="stat-value">$453.57</span></div>
  <div class="abs tick-sep" style="left:826px"></div>
  <div class="abs stat" style="left:844px"><span class="stat-label">24h Volume</span><span class="stat-value">7194 BTC</span></div>
</section>

<section class="abs panel pairs" style="left:26px;top:190px">
  <div class="th-split"><span>Pair</span><span>Price</span></div>
  <table class="data-table">
    <tr><td>BTC / USD</td><td><span class="down">↓</span> 634.12</td></tr>
    <tr><td>LTC / USD</td><td><span class="down">↓</span> 634.12</td></tr>
    <tr><td>LTC / BTC</td><td><span class="up">↑</span> 634.12</td></tr>
    <tr><td></td><td></td></tr>
    <tr><td></td><td></td></tr>
  </table>
</section>

<section class="abs panel balance" style="left:26px;top:389px">
  <div class="panel-head"><span>Your Balance</span></div>
  <table class="data-table">
    <tr><td>BTC</td><td>0.92176</td></tr>
    <tr><td>LTC</td><td>0</td></tr>
    <tr><td>USD</td><td>1987.45</td></tr>
    <tr><td></td><td></td></tr>
    <tr><td></td><td></td></tr>
  </table>
</section>

<section class="abs panel chat">
  <div class="tabs"><span class="active">Chat</span><span>News</span><span>Chirper</span></div>
  <div class="chat-msg"><span class="chat-user">User 1</span><span class="chat-text">How are you doing?</span></div>
  <div class="chat-msg"><span class="chat-user">User 1</span><span class="chat-text">How are you doing?</span></div>
  <div class="chat-msg"><span class="chat-user">User 1</span><span class="chat-text">How are you doing?</span></div>
  <div class="chat-input">Type your message here</div>
</section>

<section class="abs chart-panel">
  <div class="abs toolbar-item" style="left:12px;width:125px"></div>
  <div class="abs toolbar-item" style="left:137px;width:47px">1D<span class="caret"></span></div>
  <div class="abs toolbar-item" style="left:198px;width:149px">Chart<span class="caret"></span></div>
  <div class="abs toolbar-item" style="left:359px;width:147px">Studies<span class="caret" style="background:#ddd"></span></div>
  <div class="abs toolbar-item" style="left:519px;width:70px">
    <svg width="20" height="19" viewBox="0 0 20 19"><circle cx="10" cy="9.5" r="6" fill="none" stroke="#555" stroke-width="3" stroke-dasharray="3 2"/><circle cx="10" cy="9.5" r="3" fill="none" stroke="#555" stroke-width="2"/></svg>
    <span class="caret" style="background:#fff"></span>
  </div>
  <div class="abs toolbar-item" style="left:591px;width:34px;text-align:center">F</div>

  <div class="abs chart-area">
    <svg width="637" height="423" viewBox="0 0 637 423" role="img" aria-label="Candlestick price chart, July to November">
      <g stroke="var(--grid)" stroke-width="1">
        <line x1="0" x2="580" y1="54" y2="54"/><line x1="0" x2="580" y1="79" y2="79"/>
        <line x1="0" x2="580" y1="104" y2="104"/><line x1="0" x2="580" y1="130" y2="130"/>
        <line x1="0" x2="580" y1="155" y2="155"/><line x1="0" x2="580" y1="180" y2="180"/>
        <line x1="0" x2="580" y1="205" y2="205"/><line x1="0" x2="580" y1="230" y2="230"/>
        <line x1="0" x2="580" y1="256" y2="256"/><line x1="0" x2="580" y1="281" y2="281"/>
        <line x1="0" x2="580" y1="306" y2="306"/><line x1="0" x2="580" y1="331" y2="331"/>
        <line x1="0" x2="580" y1="359" y2="359"/>
        <line x1="129" x2="129" y1="0" y2="400"/><line x1="264" x2="264" y1="0" y2="400"/>
        <line x1="376" x2="376" y1="0" y2="400"/><line x1="500" x2="500" y1="0" y2="400"/>
      </g>
      <g transform="translate(0,3783.6) scale(1,-25.2)">
        <g class="bull" fill="#7fbf6a" stroke="#7fbf6a">
          <line x1="11.5" x2="11.5" y1="136.6" y2="137.8" vector-effect="non-scaling-stroke"/><rect x="8" y="136.8" width="7" height="0.7"/>
          <line x1="40.9" x2="40.9" y1="136.8" y2="137.9" vector-effect="non-scaling-stroke"/><rect x="37.4" y="137.0" width="7" height="0.6"/>
          <line x1="70.3" x2="70.3" y1="136.9" y2="139.0" vector-effect="non-scaling-stroke"/><rect x="66.8" y="137.1" width="7" height="1.2"/>
          <line x1="85" x2="85" y1="138.0" y2="140.0" vector-effect="non-scaling-stroke"/><rect x="81.5" y="138.4" width="7" height="1.2"/>
          <line x1="99.7" x2="99.7" y1="139.2" y2="140.9" vector-effect="non-scaling-stroke"/><rect x="96.2" y="139.5" width="7" height="0.8"/>
          <line x1="114.4" x2="114.4" y1="139.8" y2="141.3" vector-effect="non-scaling-stroke"/><rect x="110.9" y="140.2" width="7" height="0.7"/>
          <line x1="129.1" x2="129.1" y1="140.6" y2="142.0" vector-effect="non-scaling-stroke"/><rect x="125.6" y="140.9" width="7" height="0.6"/>
          <line x1="158.5" x2="158.5" y1="140.3" y2="141.6" vector-effect="non-scaling-stroke"/><rect x="155" y="140.7" width="7" height="0.6"/>
          <line x1="173.2" x2="173.2" y1="141.0" y2="142.4" vector-effect="non-scaling-stroke"/><rect x="169.7" y="141.3" width="7" height="0.6"/>
          <line x1="187.9" x2="187.9" y1="141.8" y2="143.6" vector-effect="non-scaling-stroke"/><rect x="184.4" y="142.0" width="7" height="1.2"/>
          <line x1="202.6" x2="202.6" y1="143.0" y2="144.8" vector-effect="non-scaling-stroke"/><rect x="199.1" y="143.2" width="7" height="1.1"/>
          <line x1="217.3" x2="217.3" y1="143.8" y2="144.9" vector-effect="non-scaling-stroke"/><rect x="213.8" y="144.3" width="7" height="0.15"/>
          <line x1="232" x2="232" y1="144.4" y2="147.4" vector-effect="non-scaling-stroke"/><rect x="228.5" y="144.6" width="7" height="1.9"/>
          <line x1="246.7" x2="246.7" y1="146.3" y2="148.0" vector-effect="non-scaling-stroke"/><rect x="243.2" y="146.6" width="7" height="0.6"/>
          <line x1="317.3" x2="317.3" y1="143.5" y2="145.4" vector-effect="non-scaling-stroke"/><rect x="313.8" y="143.8" width="7" height="1.2"/>
          <line x1="346.7" x2="346.7" y1="144.1" y2="146.0" vector-effect="non-scaling-stroke"/><rect x="343.2" y="144.3" width="7" height="1.3"/>
          <line x1="361.4" x2="361.4" y1="145.4" y2="147.4" vector-effect="non-scaling-stroke"/><rect x="357.9" y="145.8" width="7" height="1.2"/>
          <line x1="405.5" x2="405.5" y1="143.4" y2="145.6" vector-effect="non-scaling-stroke"/><rect x="402" y="143.8" width="7" height="1.4"/>
          <line x1="420.2" x2="420.2" y1="145.0" y2="146.8" vector-effect="non-scaling-stroke"/><rect x="416.7" y="145.4" width="7" height="0.8"/>
          <line x1="478.9" x2="478.9" y1="140.8" y2="142.4" vector-effect="non-scaling-stroke"/><rect x="475.4" y="141.2" width="7" height="0.8"/>
          <line x1="508.3" x2="508.3" y1="141.0" y2="143.4" vector-effect="non-scaling-stroke"/><rect x="504.8" y="141.3" width="7" height="1.3"/>
          <line x1="567.1" x2="567.1" y1="136.8" y2="139.2" vector-effect="non-scaling-stroke"/><rect x="563.6" y="137.0" width="7" height="1.6"/>
          <line x1="581.8" x2="581.8" y1="138.3" y2="139.6" vector-effect="non-scaling-stroke"/><rect x="578.3" y="138.6" width="7" height="0.7"/>
        </g>
        <g class="bear" fill="#c0321f" stroke="#c0321f">
          <line x1="26.2" x2="26.2" y1="136.7" y2="137.6" vector-effect="non-scaling-stroke"/><rect x="22.7" y="136.9" width="7" height="0.4"/>
          <line x1="55.6" x2="55.6" y1="136.8" y2="137.7" vector-effect="non-scaling-stroke"/><rect x="52.1" y="137.0" width="7" height="0.5"/>
          <line x1="143.8" x2="143.8" y1="140.2" y2="141.8" vector-effect="non-scaling-stroke"/><rect x="140.3" y="140.6" width="7" height="0.9"/>
          <line x1="261.4" x2="261.4" y1="145.8" y2="147.3" vector-effect="non-scaling-stroke"/><rect x="257.9" y="146.4" width="7" height="0.7"/>
          <line x1="276.1" x2="276.1" y1="144.3" y2="146.9" vector-effect="non-scaling-stroke"/><rect x="272.6" y="144.8" width="7" height="1.8"/>
          <line x1="290.8" x2="290.8" y1="143.2" y2="145.2" vector-effect="non-scaling-stroke"/><rect x="287.3" y="143.6" width="7" height="1.4"/>
          <line x1="332" x2="332" y1="143.8" y2="145.5" vector-effect="non-scaling-stroke"/><rect x="328.5" y="144.2" width="7" height="0.8"/>
          <line x1="376.1" x2="376.1" y1="144.8" y2="147.0" vector-effect="non-scaling-stroke"/><rect x="372.6" y="145.2" width="7" height="1.6"/>
          <line x1="390.8" x2="390.8" y1="143.2" y2="145.3" vector-effect="non-scaling-stroke"/><rect x="387.3" y="143.6" width="7" height="1.4"/>
          <line x1="434.9" x2="434.9" y1="144.3" y2="146.3" vector-effect="non-scaling-stroke"/><rect x="431.4" y="144.6" width="7" height="1.4"/>
          <line x1="449.6" x2="449.6" y1="142.0" y2="144.8" vector-effect="non-scaling-stroke"/><rect x="446.1" y="142.4" width="7" height="2.2"/>
          <line x1="464.3" x2="464.3" y1="140.7" y2="142.6" vector-effect="non-scaling-stroke"/><rect x="460.8" y="141.0" width="7" height="1.3"/>
          <line x1="493.6" x2="493.6" y1="140.8" y2="142.3" vector-effect="non-scaling-stroke"/><rect x="490.1" y="141.2" width="7" height="0.8"/>
          <line x1="523" x2="523" y1="140.2" y2="142.8" vector-effect="non-scaling-stroke"/><rect x="519.5" y="140.5" width="7" height="2.1"/>
          <line x1="537.7" x2="537.7" y1="138.3" y2="140.7" vector-effect="non-scaling-stroke"/><rect x="534.2" y="138.6" width="7" height="1.8"/>
          <line x1="552.4" x2="552.4" y1="136.6" y2="139.0" vector-effect="non-scaling-stroke"/><rect x="548.9" y="136.9" width="7" height="1.8"/>
        </g>
      </g>
      <g fill="#eee" font-size="11" font-family="Open Sans, Arial, sans-serif">
        <text x="590" y="58">148.00</text><text x="590" y="83">147.00</text>
        <text x="590" y="108">146.00</text><text x="590" y="134">145.00</text>
        <text x="590" y="159">144.00</text><text x="590" y="184">143.00</text>
        <text x="590" y="234">141.00</text><text x="590" y="260">140.00</text>
        <text x="590" y="285">139.00</text><text x="590" y="310">138.00</text>
        <text x="590" y="335">137.00</text><text x="590" y="363">129.00</text>
        <text x="590" y="386">128.00</text>
      </g>
      <rect x="586" y="194" width="42" height="17" rx="2" fill="#6aa84f"/>
      <text x="591" y="207" fill="#fff" font-size="11" font-family="Open Sans, Arial, sans-serif">142.14</text>
      <circle cx="170" cy="373" r="10" fill="#444"/><rect x="165" y="372" width="10" height="2" fill="#fff"/>
      <path d="M190 376 L262 369 L262 373 L190 379 Z" fill="#555"/>
      <circle cx="266" cy="373" r="10" fill="#444"/><rect x="261" y="372" width="10" height="2" fill="#fff"/><rect x="265" y="368" width="2" height="10" fill="#fff"/>
      <rect x="584" y="368" width="42" height="24" rx="3" fill="#aaa"/>
      <path d="M593 377 H606 V373 L613 380 L606 387 V383 H593 Z" fill="#fff"/><rect x="615" y="373" width="2" height="14" fill="#fff"/>
      <g fill="#fff" font-size="13" font-family="Open Sans, Arial, sans-serif">
        <text x="0" y="416">jul</text><text x="116" y="416">aug</text>
        <text x="252" y="416">sep</text><text x="365" y="416">oct</text>
        <text x="488" y="416">nov</text>
      </g>
    </svg>
    <div class="abs select-tool">Select Tool</div>
    <div class="abs ohlc"><div><b>O:</b>141.93 &nbsp;&nbsp; <b>H:</b>142.10 &nbsp;&nbsp; <b>V:</b>119.9m</div><div><b>C:</b>141.02 &nbsp;&nbsp; <b>L:</b>140.80</div></div>
  </div>
</section>
<div class="abs side-caret"></div>

<section class="abs orders">
  <div class="tabs"><span class="active">Orders</span><span style="padding-left:30px">History</span><span>Transactions</span></div>
  <table class="orders-table">
    <tr><th class="c1">Ticker</th><th class="c2">Time</th><th class="c3">Price</th><th>Volume</th></tr>
    <tr><td class="c1">BTC / USD</td><td>12:23 &nbsp;/ &nbsp;12-04-2014</td><td>634.34</td><td>0.23</td></tr>
    <tr><td class="c1">LTC / USD</td><td>12:23 &nbsp;/ &nbsp;12-04-2014</td><td>23.45</td><td>0.01</td></tr>
    <tr><td class="c1"></td><td></td><td></td><td></td></tr>
    <tr><td class="c1"></td><td></td><td></td><td></td></tr>
  </table>
</section>

<section class="abs trade">
  <div class="trade-tabs"><span class="active">Market</span><span>Limit</span></div>
  <div class="quote-row">
    <div class="quote sell"><span class="quote-title">Limit SELL</span><span class="quote-price">157<strong>5.6</strong>0</span><span class="quote-qty">Qty 20.0</span></div>
    <div class="quote buy"><span class="quote-title">Limit BUY</span><span class="quote-price">157<strong>5.6</strong>1</span><span class="quote-qty">Qty 20.0</span></div>
  </div>
  <div class="order-fields">
    <div><label>Quantity</label><div class="field" style="width:70px">50</div></div>
    <div><label>Limit</label><div class="field" style="width:132px">1576.63</div></div>
  </div>
</section>

<section class="abs book">
  <div class="th-split"><span>Price</span><span>Volume</span></div>
  <table class="book-table">
    <tr class="ask"><td>123</td><td>0.233</td></tr><tr class="ask"><td>123</td><td>0.233</td></tr>
    <tr class="ask"><td>123</td><td>0.233</td></tr><tr class="ask"><td>123</td><td>0.233</td></tr>
    <tr class="ask"><td>123</td><td>0.233</td></tr><tr class="ask"><td>123</td><td>0.233</td></tr>
    <tr class="ask"><td>123</td><td>0.233</td></tr><tr class="ask"><td>123</td><td>0.233</td></tr>
  </table>
  <table class="book-table">
    <tr class="bid"><td>123</td><td>0.233</td></tr><tr class="bid"><td>123</td><td>0.233</td></tr>
    <tr class="bid"><td>123</td><td>0.233</td></tr><tr class="bid"><td>123</td><td>0.233</td></tr>
    <tr class="bid"><td>123</td><td>0.233</td></tr><tr class="bid"><td>123</td><td>0.233</td></tr>
    <tr class="bid"><td>123</td><td>0.233</td></tr><tr class="bid"><td>123</td><td>0.233</td></tr>
  </table>
</section>

<footer class="abs footer">
  <div class="abs footer-copy">2014 &nbsp;VelmoraTrade. All Rights Reserved.</div>
  <div class="abs footer-links"><span>About</span><span>Terms &amp; Conditions</span><span>FAQ</span></div>
</footer>

</body>
</html>
```